Save our Business Card - We need your help

We need a fresh look on our business cards. We like it as it is, but it's not quite getting the 'wow' effect that we desire.
We're a tech startup building a cloud based solution for retailers consisting of Point of Sale, Inventory management and CRM.
The design should communicate a sense of a company that cares about the little things, design and relationships.
You can have a look at our website www.tillnest.com to get a feel for what we're like. Please feel free to message us for any further clarification
Target Market(s)
Our Customers are retail busines owners, cafe owners, other startups etc.
Industry/Entity Type
Building
Colors
Designer to choose colors to be used in the design.
Look and feel
Each slider illustrates characteristics of the customer's brand and the style your logo design should communicate.

```html
<!DOCTYPE html>
<html lang="en">
<head>
<meta charset="utf-8">
<title>TillNest Business Card</title>
<link href="https://fonts.googleapis.com/css2?family=Open+Sans:wght@400;600;700&display=swap" rel="stylesheet">
<style>
  :root {
    --brand-orange: #ee8f1c;
    --brand-orange-deep: #e67e12;
    --card-white: #f7f7f7;
    --text-grey: #6d6d6d;
    --backdrop: #e9e7e5;
    --white: #ffffff;
  }
  * { margin: 0; padding: 0; box-sizing: border-box; }
  html, body {
    width: 1200px; height: 899px; overflow: hidden;
    background: var(--backdrop);
    font-family: "Open Sans", Arial, sans-serif;
  }
  .stage {
    position: relative; width: 1200px; height: 899px;
    display: flex; align-items: center; justify-content: center; gap: 60px;
  }
  .card {
    position: relative; width: 500px; height: 286px;
    box-shadow: 0 6px 18px rgba(0,0,0,0.12);
    overflow: hidden;
  }
  /* Front */
  .card-front {
    background: var(--brand-orange);
    display: flex; flex-direction: column; align-items: center; justify-content: center;
  }
  .brand { display: flex; align-items: center; gap: 12px; }
  .brand-mark { width: 40px; height: 40px; }
  .brand-name { font-weight: 700; font-size: 40px; letter-spacing: -0.5px; line-height: 1; }
  .card-front .brand-mark { background: var(--white); }
  .card-front .brand-name { color: var(--white); }
  .front-url {
    margin-top: 38px; color: var(--white);
    font-size: 12px; letter-spacing: 3px;
  }
  /* Back */
  .card-back { background: var(--card-white); }
  .card-back .brand {
    position: absolute; left: 36px; top: 150px;
  }
  .card-back .brand-mark { background: var(--brand-orange); }
  .card-back .brand-name { color: var(--brand-orange); font-size: 36px; }
  .contact {
    position: absolute; left: 300px; top: 42px;
    color: var(--text-grey); font-size: 11px; line-height: 1.45;
  }
  .contact-name { color: var(--brand-orange); font-size: 17px; font-weight: 600; line-height: 1.2; }
  .contact-role { font-size: 10px; margin-bottom: 12px; }
  .contact-address { margin-bottom: 12px; }
  .contact-line { display: flex; align-items: center; gap: 7px; }
  .contact-line svg { width: 10px; height: 10px; fill: var(--brand-orange); flex: none; }
  .stripe {
    position: absolute; left: 0; right: 0; bottom: 0; height: 10px;
    background: var(--brand-orange-deep);
  }
</style>
</head>
<body>
<main class="stage">
  <section class="card card-front">
    <div class="brand">
      <span class="brand-mark"></span>
      <span class="brand-name">TillNest</span>
    </div>
    <p class="front-url">www.tillnest.com</p>
  </section>

  <section class="card card-back">
    <div class="brand">
      <span class="brand-mark"></span>
      <span class="brand-name">TillNest</span>
    </div>
    <div class="contact">
      <p class="contact-name">Daniel Reyes</p>
      <p class="contact-role">President</p>
      <p class="contact-address">48 Harbor View Rd<br>Suite 12 Kailua</p>
      <p class="contact-line">
        <svg viewBox="0 0 10 10"><path d="M2 0h2l1 3-1.5 1a6 6 0 0 0 2.5 2.5L7 5l3 1v2c0 1-1 2-2 2A8 8 0 0 1 0 2c0-1 1-2 2-2z"/></svg>
        +(603) 4120 7736
      </p>
      <p class="contact-line">
        <svg viewBox="0 0 10 10"><path d="M2.5 0h5a1 1 0 0 1 1 1v8a1 1 0 0 1-1 1h-5a1 1 0 0 1-1-1V1a1 1 0 0 1 1-1zm.5 1.5v6h4v-6z"/></svg>
        +(603) 4120 7737
      </p>
      <p class="contact-line">
        <svg viewBox="0 0 10 10"><path d="M0 2h10v6H0zM0 2l5 3.5L10 2" stroke="#fff" stroke-width="0.8"/></svg>
        info@tillnest.com
      </p>
      <p class="contact-line">
        <svg viewBox="0 0 10 10"><circle cx="5" cy="5" r="5"/></svg>
        www.tillnest.com
      </p>
    </div>
    <div class="stripe"></div>
  </section>
</main>
</body>
</html>
```